Thai Takeaway Menu Design

I need a menu re-design for a thai takeaway/restaurant in australia.

Please use content from the existing menu
http://www.platterwink.example/u/menu/7302918?p=1

I'd like to emphasise on
1 - free delivery for order over $40
2 - gluten free and vegetatian option available on most meal (however you want to word it - not fuss)

*remove (the banner order online and save $10)

I'm happy to change the whole concept & design. I particularly like rustic, raw look more than moden ones. Does not need to be flowery or anything like current one :)

Industry/Entity Type

Restaurant

```html
<!DOCTYPE html>
<html lang="en">
<head>
<meta charset="utf-8">
<title>SABAI – Thai Takeaway Menu Concepts</title>
<link rel="stylesheet" href="https://fonts.googleapis.com/css2?family=Tinos:wght@400;700&family=Open+Sans:wght@400&display=swap">
<style>
  :root {
    --page: #ffffff;
    --label: #111111;
    --fold: #2a2a2a;

    --sunset-orange: #f6a51f;
    --sunset-gold: #f9c21a;
    --sunset-pink: #e7407c;
    --sunset-box: rgba(251, 176, 58, 0.85);
    --sunset-ink: #8e1c14;
    --sunset-title: #9a3d1c;

    --parchment: #efe5b4;
    --parchment-light: #f6efcf;
    --parchment-red: #b71f1d;
    --parchment-ink: #8a1a14;

    --linen: #ece5c9;
    --linen-light: #f5efd8;
    --linen-box: rgba(205, 192, 155, 0.55);
    --linen-ink: #3f3022;
    --linen-title: #7b4a1f;
    --linen-stone: #8c8a86;

    --badge-face: #fbf7ec;
  }

  * { box-sizing: border-box; margin: 0; padding: 0; }

  html, body {
    width: 1200px;
    height: 1122px;
    overflow: hidden;
    background: var(--page);
  }

  .board {
    position: relative;
    width: 1200px;
    height: 1122px;
    font-family: "Tinos", "Times New Roman", serif;
  }

  .option-label {
    position: absolute;
    font-family: "Open Sans", Arial, sans-serif;
    font-size: 15px;
    color: var(--label);
  }
  .option-label--one { left: 219px; top: 585px; }
  .option-label--two { left: 902px; top: 585px; }
  .option-label--three { left: 886px; top: 1029px; }

  /* ---------- brochure shell ---------- */
  .brochure {
    position: absolute;
    width: 560px;
    height: 400px;
    overflow: hidden;
    color: var(--ink);
  }
  .brochure--sunset { left: 5px; top: 169px; --ink: var(--sunset-ink); }
  .brochure--parchment { left: 606px; top: 171px; --ink: var(--parchment-ink); }
  .brochure--linen { left: 306px; top: 656px; --ink: var(--linen-ink); }

  .fold-frame {
    position: absolute;
    left: 0; top: 0;
    width: 374px; height: 400px;
    border: 1px solid var(--fold);
    z-index: 5;
    pointer-events: none;
  }
  .fold-frame::after {
    content: "";
    position: absolute;
    left: 186px; top: 0;
    width: 1px; height: 100%;
    background: var(--fold);
  }

  .art { position: absolute; }

  .menu-box { position: absolute; }

  .column {
    position: absolute;
    text-align: center;
    z-index: 3;
  }

  .block { position: absolute; left: 0; width: 100%; }

  .dish-heading {
    font-weight: 700;
    font-size: 8.5px;
    line-height: 11px;
    margin-bottom: 4px;
  }
  .dish-list {
    list-style: none;
    font-size: 7px;
    line-height: 8.6px;
  }
  .price {
    font-weight: 700;
    font-size: 8px;
    margin-top: 8px;
  }
  .aside {
    font-size: 6.8px;
    margin-top: 8px;
  }
  .hours-heading {
    font-weight: 700;
    font-size: 7.2px;
    margin-bottom: 9px;
  }
  .hours-line {
    font-size: 7px;
    line-height: 8.6px;
  }
  .hours-line b { font-weight: 700; }
  .hours-gap { height: 9px; }
  .address {
    font-weight: 700;
    font-size: 6.8px;
    line-height: 8.2px;
  }

  .flourish {
    position: absolute;
    left: 50%;
    width: 52px;
    height: 11px;
    margin-left: -26px;
    border-radius: 6px;
    background: var(--flourish, rgba(140, 30, 20, 0.35));
  }

  .rule {
    position: absolute;
    left: 50%;
    width: 112px;
    margin-left: -56px;
    height: 7px;
  }
  .rule svg { display: block; }

  /* ---------- cover panel ---------- */
  .cover-name {
    position: absolute;
    font-family: "Tinos", "Times New Roman", serif;
    font-weight: 400;
    letter-spacing: 1px;
    line-height: 1;
    z-index: 4;
  }
  .cover-tagline {
    position: absolute;
    font-size: 8.8px;
    line-height: 10px;
    z-index: 4;
  }
  .cover-tagline .cuisine {
    display: inline-block;
    border-bottom: 1px solid currentColor;
    padding-bottom: 1px;
    margin-bottom: 2px;
  }
  .cover-tagline .service {
    display: block;
    font-size: 7.6px;
    font-weight: 700;
  }
  .diet-note {
    position: absolute;
    font-weight: 700;
    font-size: 7px;
    line-height: 8.4px;
    z-index: 4;
  }

  .delivery-badge {
    position: absolute;
    width: 60px;
    height: 60px;
    border-radius: 50%;
    background: var(--badge-face);
    box-shadow: 3px 4px 4px rgba(0, 0, 0, 0.55);
    color: #b0201a;
    text-align: center;
    z-index: 6;
    display: flex;
    flex-direction: column;
    justify-content: center;
    transform: rotate(-14deg);
    font-weight: 700;
  }
  .delivery-badge .badge-lead { font-size: 12px; line-height: 12px; }
  .delivery-badge .badge-rest { font-size: 6.8px; line-height: 7.6px; }

  /* ---------- option one : sunset ---------- */
  .brochure--sunset .backdrop {
    left: 0; top: 0; width: 560px; height: 400px;
    background:
      linear-gradient(90deg, rgba(120, 60, 20, 0.35) 0, rgba(0,0,0,0) 3%, rgba(0,0,0,0) 97%, rgba(120, 60, 20, 0.3) 100%),
      linear-gradient(90deg, var(--sunset-orange) 0%, #f8b420 55%, #f4a21c 66%, #ef7e3a 80%, var(--sunset-pink) 100%);
  }
  .brochure--sunset .cover-wash {
    left: 374px; top: 0; width: 186px; height: 400px;
    background:
      radial-gradient(ellipse at 85% 25%, rgba(231, 50, 130, 0.8), rgba(231, 50, 130, 0) 60%),
      linear-gradient(180deg, rgba(240, 110, 60, 0.2), rgba(249, 194, 26, 0.5) 100%);
  }
  .brochure--sunset .cover-foot {
    left: 374px; top: 345px; width: 186px; height: 55px;
    background: var(--sunset-gold);
  }
  .brochure--sunset .pagoda-art {
    left: 396px; top: 100px; width: 108px; height: 250px;
    background: linear-gradient(180deg, rgba(232, 60, 110, 0.55), rgba(200, 40, 90, 0.45) 60%, rgba(240, 120, 60, 0.2));
    border-radius: 40% 40% 4px 4px / 20% 20% 4px 4px;
  }
  .brochure--sunset .fish-art {
    left: 118px; top: 40px; width: 150px; height: 260px;
    background: radial-gradient(ellipse at center, rgba(226, 110, 40, 0.35), rgba(226, 110, 40, 0) 70%);
  }
  .brochure--sunset .menu-box { background: var(--sunset-box); }
  .brochure--sunset .box-a { left: 16px; top: 13px; width: 157px; height: 369px; }
  .brochure--sunset .box-b { left: 201px; top: 13px; width: 159px; height: 186px; }
  .brochure--sunset .box-c { left: 201px; top: 210px; width: 159px; height: 172px; }
  .brochure--sunset .col-one { left: 16px; top: 0; width: 157px; height: 400px; }
  .brochure--sunset .col-two { left: 201px; top: 0; width: 159px; height: 400px; }
  .brochure--sunset .cover-name { left: 396px; top: 44px; font-size: 40px; color: var(--sunset-title); }
  .brochure--sunset .cover-tagline { left: 400px; top: 84px; color: var(--sunset-title); }
  .brochure--sunset .diet-note { left: 386px; top: 361px; color: var(--sunset-ink); }
  .brochure--sunset .delivery-badge { left: 497px; top: 306px; }

  /* ---------- option two : parchment ---------- */
  .brochure--parchment .backdrop {
    left: 0; top: 0; width: 560px; height: 400px;
    background:
      linear-gradient(180deg, rgba(230, 210, 130, 0.5) 0%, rgba(0,0,0,0) 20%, rgba(230, 205, 120, 0.45) 45%, rgba(0,0,0,0) 65%),
      linear-gradient(90deg, var(--parchment) 0%, var(--parchment-light) 50%, var(--parchment) 100%);
  }
  .brochure--parchment .skyline-art {
    left: 0; top: 290px; width: 560px; height: 110px;
    background: linear-gradient(180deg, rgba(183, 31, 29, 0) 0%, rgba(183, 31, 29, 0.85) 25%, var(--parchment-red) 45%, #a31a18 100%);
  }
  .brochure--parchment .temple-art {
    left: 384px; top: 188px; width: 176px; height: 130px;
    background: linear-gradient(180deg, rgba(183, 31, 29, 0.2), rgba(183, 31, 29, 0.75));
    border-radius: 50% 50% 0 0 / 30% 30% 0 0;
  }
  .brochure--parchment .col-one { left: 14px; top: 0; width: 172px; height: 400px; }
  .brochure--parchment .col-two { left: 196px; top: 0; width: 172px; height: 400px; }
  .brochure--parchment .cover-name { left: 418px; top: 57px; font-size: 38px; color: #7a4a22; }
  .brochure--parchment .cover-tagline { left: 421px; top: 94px; color: #7a4a22; }
  .brochure--parchment .diet-note { left: 384px; top: 352px; color: #ffffff; }
  .brochure--parchment .address { color: #ffffff; }
  .brochure--parchment .delivery-badge { left: 500px; top: 311px; }
  .brochure--parchment { --flourish: rgba(160, 30, 25, 0.4); }

  /* ---------- option three : linen ---------- */
  .brochure--linen .backdrop {
    left: 0; top: 0; width: 560px; height: 400px;
    background:
      radial-gradient(circle at 20% 30%, rgba(200, 190, 150, 0.4), rgba(0,0,0,0) 30%),
      radial-gradient(circle at 55% 70%, rgba(200, 190, 150, 0.35), rgba(0,0,0,0) 30%),
      linear-gradient(90deg, var(--linen) 0%, var(--linen) 66%, var(--linen-light) 72%, var(--linen-light) 100%);
  }
  .brochure--linen .carving-art {
    left: 469px; top: 0; width: 91px; height: 400px;
    background: linear-gradient(90deg, rgba(140, 138, 134, 0) 0%, rgba(140, 138, 134, 0.55) 35%, var(--linen-stone) 70%, #a8a6a0 100%);
  }
  .brochure--linen .menu-box { background: var(--linen-box); }
  .brochure--linen .box-a { left: 22px; top: 70px; width: 142px; height: 256px; }
  .brochure--linen .box-b { left: 208px; top: 70px; width: 142px; height: 104px; }
  .brochure--linen .col-one { left: 22px; top: 0; width: 142px; height: 400px; }
  .brochure--linen .col-two { left: 208px; top: 0; width: 142px; height: 400px; }
  .brochure--linen .cover-name { left: 386px; top: 56px; font-size: 36px; color: var(--linen-title); }
  .brochure--linen .cover-tagline { left: 389px; top: 92px; color: var(--linen-title); }
  .brochure--linen .diet-note { left: 384px; top: 354px; color: var(--linen-ink); }
  .brochure--linen .delivery-badge { left: 497px; top: 330px; }
  .brochure--linen { --flourish: rgba(60, 45, 30, 0.4); }
</style>
</head>
<body>
<main class="board">

  <!-- Concept one: sunset wash -->
  <section class="brochure brochure--sunset" aria-label="Menu concept one">
    <div class="art backdrop" role="img" aria-label="Grungy orange and magenta painted texture"></div>
    <div class="art fish-art" role="img" aria-label="Faint line illustration of a koi fish"></div>
    <div class="art cover-wash"></div>
    <div class="art cover-foot"></div>
    <div class="art pagoda-art" role="img" aria-label="Magenta pagoda illustration"></div>
    <div class="menu-box box-a"></div>
    <div class="menu-box box-b"></div>
    <div class="menu-box box-c"></div>
    <div class="fold-frame"></div>

    <div class="column col-one">
      <span class="flourish" style="top:44px" role="img" aria-label="Ornamental flourish"></span>
      <div class="block" style="top:69px">
        <h3 class="dish-heading">Dinner for Two</h3>
        <ul class="dish-list"><li>Spring Rolls (4)</li><li>Chicken &amp; Cashew Nuts</li><li>Massaman Curry</li><li>Rice</li></ul>
        <p class="price">$28</p>
      </div>
      <span class="rule" style="top:175px"><svg width="112" height="7"><line x1="0" y1="3.5" x2="112" y2="3.5" stroke="#8e1c14" stroke-width="0.8"/><path d="M2 3.5l3-2v4z M110 3.5l-3-2v4z M56 1l2.5 2.5L56 6l-2.5-2.5z" fill="#8e1c14"/></svg></span>
      <div class="block" style="top:220px">
        <h3 class="dish-heading">Family Pack</h3>
        <ul class="dish-list"><li>Spring Rolls (4)</li><li>Satay Chicken (4)</li><li>Chicken &amp; Cashew Nuts</li><li>Red Curry Beef</li><li>Pad Thai</li><li>Rice (L)</li></ul>
        <p class="price">$45</p>
      </div>
      <span class="flourish" style="top:349px" role="img" aria-label="Ornamental flourish"></span>
    </div>

    <div class="column col-two">
      <span class="flourish" style="top:44px" role="img" aria-label="Ornamental flourish"></span>
      <div class="block" style="top:69px">
        <h3 class="dish-heading">Lunch Special $10</h3>
        <ul class="dish-list"><li>Pad Thai</li><li>Sweet and Sour Pork / w Rice</li><li>Chicken &amp; Cashew Nuts / w Rice</li><li>Green Curry Chicken / wRice</li><li>Beef Noodle Soup</li></ul>
        <p class="aside">(Free Can of Soft Drink)</p>
      </div>
      <span class="flourish" style="top:183px" role="img" aria-label="Ornamental flourish"></span>
      <div class="block" style="top:246px">
        <h4 class="hours-heading">Trading Hours</h4>
        <p class="hours-line"><b>Lunch</b> (Wednesday - Sunday)</p>
        <p class="hours-line">Timings: 11.00 - 2.30 PM</p>
        <div class="hours-gap"></div>
        <p class="hours-line"><b>Dinner</b> (7 days)</p>
        <p class="hours-line">Timings: 5.00 - 9.30 PM</p>
      </div>
      <span class="rule" style="top:324px"><svg width="112" height="7"><line x1="0" y1="3.5" x2="112" y2="3.5" stroke="#8e1c14" stroke-width="0.8"/><path d="M2 3.5l3-2v4z M110 3.5l-3-2v4z M56 1l2.5 2.5L56 6l-2.5-2.5z" fill="#8e1c14"/></svg></span>
      <div class="block" style="top:341px">
        <p class="address">62 Kelvin Road, Bramble Park<br>Corner of Hollis St. and Kelvin Rd.<br>Phone: 07 3900 4417</p>
      </div>
    </div>

    <h2 class="cover-name">SABAI</h2>
    <p class="cover-tagline"><span class="cuisine">Traditional Thai Cuisine</span><span class="service">Dine In, Takeaway &amp; Delivery</span></p>
    <p class="diet-note">* Gluten free &amp; vegetation<br>&nbsp;&nbsp;option available on most meal</p>
    <div class="delivery-badge"><span class="badge-lead">*FREE</span><span class="badge-rest">delivery for<br>order<br>over $40</span></div>
  </section>

  <!-- Concept two: parchment and red skyline -->
  <section class="brochure brochure--parchment" aria-label="Menu concept two">
    <div class="art backdrop" role="img" aria-label="Weathered cream parchment texture"></div>
    <div class="art temple-art" role="img" aria-label="Red ink pagoda and blossom tree illustration"></div>
    <div class="art skyline-art" role="img" aria-label="Red painted Thai temple skyline along the bottom"></div>
    <div class="fold-frame"></div>

    <div class="column col-one">
      <span class="flourish" style="top:40px" role="img" aria-label="Ornamental flourish"></span>
      <div class="block" style="top:64px">
        <h3 class="dish-heading">Dinner for Two</h3>
        <ul class="dish-list"><li>Spring Rolls (4)</li><li>Chicken &amp; Cashew Nuts</li><li>Massaman Curry</li><li>Rice</li></ul>
        <p class="price">$28</p>
      </div>
      <span class="rule" style="top:160px"><svg width="112" height="7"><line x1="0" y1="3.5" x2="112" y2="3.5" stroke="#8a1a14" stroke-width="0.8"/><path d="M56 1l2.5 2.5L56 6l-2.5-2.5z" fill="#8a1a14"/></svg></span>
      <div class="block" style="top:182px">
        <h3 class="dish-heading">Family Pack</h3>
        <ul class="dish-list"><li>Spring Rolls (4)</li><li>Satay Chicken (4)</li><li>Chicken &amp; Cashew Nuts</li><li>Red Curry Beef</li><li>Pad Thai</li><li>Rice (L)</li></ul>
        <p class="price">$45</p>
      </div>
    </div>

    <div class="column col-two">
      <span class="flourish" style="top:40px" role="img" aria-label="Ornamental flourish"></span>
      <div class="block" style="top:64px">
        <h3 class="dish-heading">Lunch Special $10</h3>
        <ul class="dish-list"><li>Pad Thai</li><li>Sweet and Sour Pork / w Rice</li><li>Chicken &amp; Cashew Nuts / w Rice</li><li>Green Curry Chicken / wRice</li><li>Beef Noodle Soup</li></ul>
        <p class="aside">(Free Can of Soft Drink)</p>
      </div>
      <span class="rule" style="top:168px"><svg width="112" height="7"><line x1="0" y1="3.5" x2="112" y2="3.5" stroke="#8a1a14" stroke-width="0.8"/><path d="M56 1l2.5 2.5L56 6l-2.5-2.5z" fill="#8a1a14"/></svg></span>
      <div class="block" style="top:192px">
        <h4 class="hours-heading">Trading Hours</h4>
        <p class="hours-line"><b>Lunch</b> (Wednesday - Sunday)</p>
        <p class="hours-line">Timings: 11.00 - 2.30 PM</p>
        <div class="hours-gap"></div>
        <p class="hours-line"><b>Dinner</b> (7 days)</p>
        <p class="hours-line">Timings: 5.00 - 9.30 PM</p>
      </div>
      <div class="block" style="top:349px">
        <p class="address">62 Kelvin Road, Bramble Park<br>Corner of Hollis St. and Kelvin Rd.<br>Phone: 07 3900 4417</p>
      </div>
    </div>

    <h2 class="cover-name">SABAI</h2>
    <p class="cover-tagline"><span class="cuisine">Traditional Thai Cuisine</span><span class="service">Dine In, Takeaway &amp; Delivery</span></p>
    <p class="diet-note">* Gluten free &amp; vegetatian<br>&nbsp;&nbsp;option available on most meal</p>
    <div class="delivery-badge"><span class="badge-lead">*FREE</span><span class="badge-rest">delivery for<br>order<br>over $40</span></div>
  </section>

  <!-- Concept three: linen and carved stone -->
  <section class="brochure brochure--linen" aria-label="Menu concept three">
    <div class="art backdrop" role="img" aria-label="Faded cream paisley pattern texture"></div>
    <div class="art carving-art" role="img" aria-label="Grey carved stone Thai temple relief"></div>
    <div class="menu-box box-a"></div>
    <div class="menu-box box-b"></div>

    <div class="column col-one">
      <span class="flourish" style="top:40px" role="img" aria-label="Ornamental flourish"></span>
      <div class="block" style="top:76px">
        <h3 class="dish-heading">Dinner for Two</h3>
        <ul class="dish-list"><li>Spring Rolls (4)</li><li>Chicken &amp; Cashew Nuts</li><li>Massaman Curry</li><li>Rice</li></ul>
        <p class="price">$28</p>
      </div>
      <span class="rule" style="top:179px"><svg width="112" height="7"><line x1="0" y1="3.5" x2="112" y2="3.5" stroke="#3f3022" stroke-width="0.8"/><path d="M56 1l2.5 2.5L56 6l-2.5-2.5z" fill="#3f3022"/></svg></span>
      <div class="block" style="top:223px">
        <h3 class="dish-heading">Family Pack</h3>
        <ul class="dish-list"><li>Spring Rolls (4)</li><li>Satay Chicken (4)</li><li>Chicken &amp; Cashew Nuts</li><li>Red Curry Beef</li><li>Pad Thai</li><li>Rice (L)</li></ul>
        <p class="price">$45</p>
      </div>
      <span class="flourish" style="top:341px" role="img" aria-label="Ornamental flourish"></span>
    </div>

    <div class="column col-two">
      <span class="flourish" style="top:40px" role="img" aria-label="Ornamental flourish"></span>
      <div class="block" style="top:76px">
        <h3 class="dish-heading">Lunch Special $10</h3>
        <ul class="dish-list"><li>Pad Thai</li><li>Sweet and Sour Pork / w Rice</li><li>Chicken &amp; Cashew Nuts / w Rice</li><li>Green Curry Chicken / wRice</li><li>Beef Noodle Soup</li></ul>
        <p class="aside">(Free Can of Soft Drink)</p>
      </div>
      <span class="flourish" style="top:193px" role="img" aria-label="Ornamental flourish"></span>
      <span class="rule" style="top:225px"><svg width="112" height="7"><line x1="0" y1="3.5" x2="112" y2="3.5" stroke="#3f3022" stroke-width="0.8"/><path d="M56 1l2.5 2.5L56 6l-2.5-2.5z" fill="#3f3022"/></svg></span>
      <div class="block" style="top:244px">
        <h4 class="hours-heading">Trading Hours</h4>
        <p class="hours-line"><b>Lunch</b> (Wednesday - Sunday)</p>
        <p class="hours-line">Timings: 11.00 - 2.30 PM</p>
        <div class="hours-gap"></div>
        <p class="hours-line"><b>Dinner</b> (7 days)</p>
        <p class="hours-line">Timings: 5.00 - 9.30 PM</p>
      </div>
      <div class="block" style="top:340px">
        <p class="address">62 Kelvin Road, Bramble Park<br>Corner of Hollis St. and Kelvin Rd.<br>Phone: 07 3900 4417</p>
      </div>
    </div>

    <h2 class="cover-name">SABAI</h2>
    <p class="cover-tagline"><span class="cuisine">Traditional Thai Cuisine</span><span class="service">Dine In, Takeaway &amp; Delivery</span></p>
    <p class="diet-note">* Gluten free &amp; vegetatian<br>&nbsp;&nbsp;option available on most meal</p>
    <div class="delivery-badge"><span class="badge-lead">*FREE</span><span class="badge-rest">delivery for<br>order<br>over $40</span></div>
  </section>

  <p class="option-label option-label--one">Option 1</p>
  <p class="option-label option-label--two">Option 2</p>
  <p class="option-label option-label--three">Option 3</p>

</main>
</body>
</html>
```